Board design for computer game

The goal of the project is to design a stunningly beautiful, elegant, board design for a Windows 8 backgammon game.
There are six elements to create:
1) The board – this is the most important one, 80% of the effort should go to this. The design should also have a 'background' layer that I can use to fill the background that will show when showing the board in different screen sizes.
2) The pieces – 15% of the effort go to the pieces
3) The background image for all other screens except the ‘game board’
4) The dice
5) The ‘button’ and 'touch' elements (On and Off)
6) other elements needed, e.g. the background for all the screens, some buttons, etc.
The game already exists in Windows Phone, and now I want to make a version for Windows 8 (which has much larger screen sizes, and can run in many different resolutions, some wide, some tall). I want to be able to have a new Windows 8 design that takes the good ideas from the existing game, but with a much more professional design that looks amazing in the larger Windows 8 screens.
Some important notes:
- the graphics have to be 'resizable' in the design program so I can save different sizes. This is key as the screen sizes for Windows 8 start at 1024x768 and could grow up to 2600x1600
- the graphic elements needed are the same as for the existing Windows 8 game
- the color palette should clearly shows the dark/light pieces (some of the players don't have good eyesight), and colors have to be pleasing (some players play 10+ hours continously)
- the design should look 'realistic' as much as possible, when applicable.
- The design has to be able to accommodate the all the information and options that exist in the current design (but of course can be modified, put in different places, etc.).
- I will require going through several revisions of all the elements. The graphics are what will sell (or not sell!) the game.
- please review the briefing doc that is included, as well as the existing graphics I have from my existing game (to take ideas on how the graphics are used)
Thanks!
FYI, there are two designs I like, that could be used as models to follow:
PlankTrove for the Slatepad: http://apps.quillmarket.example/us/app/planktrove-play-many-games/id551820367?mt=8 (the wood version)
The Tall Amber board designs: http://glyphmill.example/design/detail/tallamber and http://apps.quillmarket.example/us/app/tall-amber-chess/id472913058?mt=8&ign-mpt=uo%3D4
Updates
Hi, I have received a design that I find fits exactly what I am looking for, and will be chosing that one. Appreciate your interest in participating, but there is no need to submit designs to the project.
Thank you
Target Market(s)
Advanced backgammon players that will play in Windows 8 new tablet computers. Screen sizes vary from 1024x768 up to 2500x1600, and with different screen aspect ratios (4:3, 6:4, 10:6).
Industry/Entity Type
Computer
Requirements
Must have
- Elegant, as realistic looking as possible, stunning looks, excellent 'visibility' (the pieces have to be clearly visible).
Design has be done in such a way that it can be saved in different resolutions (keeping aspect ratio the same), and not losing the information due to compression (e.g. JPG output is not enough, probably designed in Illustrator).
Will require all the original files, so I can continue to make adjustments as the game evolves.
Nice to have
- take ideas from the two concepts I mentioned in the briefing that I like.
Use illustrator and/or photoshop.

```html
<!DOCTYPE html>
<html lang="en">
<head>
<meta charset="utf-8">
<title>Game Buttons</title>
<link rel="stylesheet" href="https://fonts.googleapis.com/css2?family=Arimo:wght@400&display=swap">
<style>
  :root {
    --canvas-bg: #ffffff;
    --red-deep: #6e0000;
    --red-mid: #b80000;
    --red-bright: #e00000;
    --red-edge: #5a0000;
    --wood-dark: #7a5430;
    --wood-mid: #a67c4e;
    --wood-light: #c49a68;
    --wood-edge: #5e3d1e;
    --label: #ffffff;
    --shadow: rgba(0, 0, 0, 0.55);
  }
  html, body {
    margin: 0;
    padding: 0;
    overflow: hidden;
    background: var(--canvas-bg);
  }
  .canvas {
    position: relative;
    width: 1200px;
    height: 352px;
    background: var(--canvas-bg);
    overflow: hidden;
    font-family: "Arimo", Arial, sans-serif;
  }
  .button {
    position: absolute;
    display: flex;
    align-items: center;
    justify-content: center;
    border-radius: 6px;
    color: var(--label);
    font-size: 30px;
    letter-spacing: 0.2px;
    box-shadow: 0 3px 10px 1px var(--shadow);
    overflow: hidden;
    box-sizing: border-box;
  }
  .button::after {
    content: "";
    position: absolute;
    inset: 0;
    background: linear-gradient(200deg, rgba(0,0,0,0.35) 0%, rgba(0,0,0,0) 22%, rgba(255,255,255,0.10) 23%, rgba(255,255,255,0) 45%);
    pointer-events: none;
  }
  .button span { position: relative; z-index: 1; }
  .button--red {
    border: 1px solid var(--red-edge);
    background:
      radial-gradient(ellipse at 45% 50%, var(--red-bright) 0%, var(--red-mid) 55%, var(--red-deep) 100%);
    text-shadow: 0 1px 1px rgba(80, 0, 0, 0.5);
  }
  .button--wood {
    border: 1px solid var(--wood-edge);
    background:
      linear-gradient(100deg, var(--wood-mid) 0%, var(--wood-light) 30%, var(--wood-mid) 55%, var(--wood-dark) 100%);
    font-size: 22px;
    text-shadow: 0 1px 1px rgba(60, 30, 10, 0.6);
  }
  .btn-undo    { left: 187px; top: 60px;  width: 163px; height: 70px; }
  .btn-back    { left: 411px; top: 60px;  width: 161px; height: 70px; }
  .btn-backup  { left: 634px; top: 60px;  width: 163px; height: 70px; }
  .btn-home    { left: 862px; top: 60px;  width: 154px; height: 66px; font-size: 28px; }
  .btn-accept  { left: 81px;  top: 192px; width: 162px; height: 74px; }
  .btn-ok      { left: 306px; top: 196px; width: 159px; height: 68px; }
  .btn-no      { left: 525px; top: 192px; width: 153px; height: 68px; }
  .btn-yes     { left: 744px; top: 192px; width: 153px; height: 66px; }
  .btn-roll    { left: 957px; top: 187px; width: 164px; height: 73px; }
</style>
</head>
<body>
<div class="canvas">
  <div class="button button--red btn-undo"><span>Undo</span></div>
  <div class="button button--red btn-back"><span>Back</span></div>
  <div class="button button--red btn-backup"><span>BackUp</span></div>
  <div class="button button--red btn-home"><span>Home</span></div>

  <div class="button button--wood btn-accept" role="img" aria-label="Wood-grain button labelled Accept"><span>Accept</span></div>
  <div class="button button--red btn-ok"><span>Ok</span></div>
  <div class="button button--red btn-no"><span>No</span></div>
  <div class="button button--red btn-yes"><span>Yes</span></div>
  <div class="button button--wood btn-roll" role="img" aria-label="Wood-grain button labelled Roll Dice"><span>Roll Dice</span></div>
</div>
</body>
</html>
```